Paw Haven Grooming Specialist Price List

Hi you know the colour scheme and the sort of style i want seeing as you designed the flyer. Prices are as follows;

FULL GROOM (bath, clipped, nails and ears)
Small Dogs £36
Medium Dogs £38
Large Dogs £40

HANDSTRIPPING (includes ears and nails)
Small Dogs £40
Medium Dogs £44
Large Dogs £48

BATHING (No extras included)
£15 all sizes

EXTRAS
Nails £5
Teeth £5
Ears £5
Anal Glands £5

```html
<!DOCTYPE html>
<html lang="en">
<head>
<meta charset="utf-8">
<title>Paw Haven Grooming Specialist – Price List</title>
<link rel="stylesheet" href="https://fonts.googleapis.com/css2?family=Arimo:wght@400;700&display=swap">
<style>
  :root {
    --red: #d4141c;
    --red-dark: #8e0a10;
    --ink: #1c1c1c;
    --white: #ffffff;
    --panel: rgba(20, 20, 20, 0.72);
    --grey-light: #e9e9e9;
    --grey-mid: #a9a9a9;
    --grey-dark: #5e5e5e;
    --coat-light: #e8cf9f;
    --coat-mid: #c9a469;
  }
  * { margin: 0; padding: 0; box-sizing: border-box; }
  html, body { width: 849px; height: 1200px; overflow: hidden; background: var(--white); }
  body { font-family: "Arimo", Arial, sans-serif; }

  .flyer {
    position: relative;
    width: 849px;
    height: 1200px;
    overflow: hidden;
    background: linear-gradient(180deg, var(--white) 0%, var(--grey-light) 18%, var(--grey-mid) 60%, var(--grey-dark) 100%);
  }

  .dog-photo {
    position: absolute;
    left: 400px;
    top: 300px;
    width: 449px;
    height: 850px;
    background:
      radial-gradient(ellipse 65% 55% at 55% 45%, var(--coat-light) 0%, var(--coat-mid) 55%, rgba(201,164,105,0) 85%);
  }

  .phone {
    position: absolute;
    left: 0; top: 0;
    width: 425px; height: 88px;
    background: linear-gradient(180deg, var(--red) 0%, var(--red-dark) 100%);
    border-bottom-right-radius: 14px;
    display: flex; align-items: center; gap: 14px;
    padding-left: 22px;
    color: var(--white);
    font-weight: 700;
    font-size: 42px;
    letter-spacing: 0.5px;
  }
  .phone svg { width: 36px; height: 36px; fill: var(--white); }

  .brand {
    position: absolute;
    left: 450px; top: 120px;
    width: 380px;
    color: var(--ink);
    font-weight: 700;
    text-align: center;
  }
  .brand-row { display: flex; align-items: center; justify-content: center; gap: 14px; white-space: nowrap; }
  .brand-mark { width: 30px; height: 30px; border-radius: 50%; background: var(--red); flex: none; }
  .brand-name { font-size: 58px; line-height: 1; }
  .brand-tagline { font-size: 30px; margin-top: 16px; white-space: nowrap; }

  .price-block { position: absolute; left: 0; width: 425px; }
  .block-head {
    background: linear-gradient(180deg, var(--red) 0%, var(--red-dark) 100%);
    color: var(--white);
    padding: 9px 22px 8px;
    border-top-right-radius: 12px;
    border-bottom-right-radius: 12px;
    box-shadow: 0 3px 8px rgba(0,0,0,0.35);
  }
  .block-title { font-size: 40px; font-weight: 700; line-height: 42px; }
  .block-note { font-size: 20px; font-weight: 700; line-height: 24px; }
  .block-list {
    list-style: none;
    background: var(--panel);
    color: var(--white);
    margin-top: 8px;
    padding: 8px 26px 8px 22px;
  }
  .block-list li {
    display: flex; justify-content: space-between;
    font-size: 36px; font-weight: 700; line-height: 45px;
  }

  .full-groom { top: 152px; }
  .handstripping { top: 410px; }
  .bathing { top: 668px; }
  .extras { top: 842px; }

  .address {
    position: absolute;
    left: 0; bottom: 0;
    width: 849px; height: 56px;
    background: rgba(15, 15, 15, 0.8);
    color: var(--white);
    display: flex; align-items: center; gap: 10px;
    padding-left: 22px;
    font-size: 25px; font-weight: 700;
  }
  .address svg { width: 24px; height: 24px; fill: var(--white); }
</style>
</head>
<body>
<main class="flyer">
  <div class="dog-photo" role="img" aria-label="Photograph of a golden Labrador with its tongue out"></div>

  <header class="phone">
    <svg viewBox="0 0 24 24" aria-hidden="true"><path d="M6.6 10.8a15.1 15.1 0 0 0 6.6 6.6l2.2-2.2c.3-.3.7-.4 1-.2 1.1.4 2.3.6 3.6.6.6 0 1 .4 1 1V20c0 .6-.4 1-1 1A17 17 0 0 1 3 4c0-.6.4-1 1-1h3.5c.6 0 1 .4 1 1 0 1.3.2 2.5.6 3.6.1.3 0 .7-.2 1z"/></svg>
    <span>07700900481</span>
  </header>

  <div class="brand">
    <div class="brand-row">
      <span class="brand-mark"></span>
      <span class="brand-name">Paw Haven</span>
    </div>
    <div class="brand-tagline">Grooming Specialist</div>
  </div>

  <section class="price-block full-groom">
    <div class="block-head">
      <h2 class="block-title">FULL GROOM</h2>
      <p class="block-note">(clipped, bath, ears and nails)</p>
    </div>
    <ul class="block-list">
      <li><span>Small Dogs</span><span>£36</span></li>
      <li><span>Medium Dogs</span><span>£38</span></li>
      <li><span>Large Dogs</span><span>£40</span></li>
    </ul>
  </section>

  <section class="price-block handstripping">
    <div class="block-head">
      <h2 class="block-title">HANDSTRIPPING</h2>
      <p class="block-note">(Includes nails and ears)</p>
    </div>
    <ul class="block-list">
      <li><span>Small Dogs</span><span>£40</span></li>
      <li><span>Medium Dogs</span><span>£44</span></li>
      <li><span>Large Dogs</span><span>£48</span></li>
    </ul>
  </section>

  <section class="price-block bathing">
    <div class="block-head">
      <h2 class="block-title">BATHING</h2>
      <p class="block-note">(No extras included)</p>
    </div>
    <ul class="block-list">
      <li><span>All sizes</span><span>£15</span></li>
    </ul>
  </section>

  <section class="price-block extras">
    <div class="block-head">
      <h2 class="block-title">EXTRAS</h2>
    </div>
    <ul class="block-list">
      <li><span>Nails</span><span>£5</span></li>
      <li><span>Teeth</span><span>£5</span></li>
      <li><span>Ears</span><span>£5</span></li>
      <li><span>Anal Glands</span><span>£5</span></li>
    </ul>
  </section>

  <footer class="address">
    <svg viewBox="0 0 24 24" aria-hidden="true"><path d="M12 3 2 12h3v8h5v-5h4v5h5v-8h3z"/></svg>
    <span>Unit 7, Meadow Court, Station Road, Oakford, Westshire</span>
  </footer>
</main>
</body>
</html>
```